Frostwyn.co - Polar Expeditions Specialists

We need a modern, visually striking business card for Frostwyn.co, a company specialized in selling expedition cruises to the most remote regions on Earth, with a focus on the Arctic and Antarctica. The design should instantly communicate that the cardholder is an expert in polar travel. Use clean, premium aesthetics with cool tones like icy blue and white, possibly incorporating polar imagery (ice, glaciers, penguins, etc.)

Attached the logo

Contact Information for Business Card

Feels high-end and trustworthy.. Visually memorable — encourages people to keep it

Colors
0054AA
0677BA
7BADD7
CADEEF
E8F1F8

Requirements
Must have
• ice, glaciers, penguins, montains
Nice to have
• modern, transparente,

```html
<!DOCTYPE html>
<html lang="en">
<head>
<meta charset="utf-8">
<title>Frostwyn.co – Business Card</title>
<link href="https://fonts.googleapis.com/css2?family=Poppins:wght@400;600&family=Inter:wght@400;500;600&display=swap" rel="stylesheet">
<style>
  :root {
    --canvas: #e0e0e0;
    --navy: #1b2340;
    --navy-deep: #15182e;
    --ink: #222433;
    --white: #ffffff;
    --ice: #eef3fb;
    --muted: #8a8a8a;
    --rule: #555555;
  }
  * { margin: 0; padding: 0; box-sizing: border-box; }
  html, body { width: 1200px; height: 1200px; overflow: hidden; }
  body { background: var(--canvas); position: relative; font-family: "Inter", sans-serif; }

  .card { position: absolute; left: 180px; width: 867px; height: 498px; overflow: hidden; }

  /* Front */
  .card-front { top: 85px; background: var(--navy); }
  .front-scene {
    position: absolute; inset: 0;
    background:
      radial-gradient(ellipse at 20% 70%, rgba(70,78,120,0.45), transparent 55%),
      radial-gradient(ellipse at 80% 60%, rgba(60,64,100,0.35), transparent 60%),
      linear-gradient(180deg, #1c2140 0%, #272742 45%, #1f2444 75%, #1a2144 100%);
  }
  .front-brand { position: absolute; left: 222px; top: 206px; display: flex; align-items: center; gap: 26px; }
  .brand-dot { width: 62px; height: 62px; border-radius: 50%; background: var(--ice); flex: none; }
  .brand-name { font-family: "Poppins", sans-serif; font-weight: 600; line-height: 1; }
  .brand-tagline { font-family: "Poppins", sans-serif; font-weight: 400; line-height: 1; margin-top: 10px; }
  .card-front .brand-name { font-size: 58px; color: var(--white); }
  .card-front .brand-tagline { font-size: 17px; color: var(--white); }

  /* Back */
  .card-back { top: 625px; background: var(--white); }
  .back-brand { position: absolute; left: 86px; top: 206px; display: flex; align-items: center; gap: 22px; }
  .card-back .brand-dot { width: 52px; height: 52px; background: var(--navy-deep); }
  .card-back .brand-name { font-size: 41px; color: var(--ink); }
  .card-back .brand-tagline { font-size: 15px; color: var(--ink); margin-top: 8px; }

  .divider { position: absolute; left: 487px; top: 124px; width: 1.5px; height: 240px; background: var(--rule); }

  .contact { position: absolute; left: 509px; top: 131px; color: #1c1c1c; }
  .contact-name { font-size: 27px; font-weight: 600; letter-spacing: 1px; line-height: 1; }
  .contact-role { font-size: 19px; color: var(--muted); margin-top: 6px; letter-spacing: 0.5px; }
  .contact-address { margin-top: 16px; font-size: 19px; font-weight: 500; letter-spacing: 2.6px; line-height: 34px; }
  .contact-list { list-style: none; margin-top: 10px; }
  .contact-list li { display: flex; align-items: center; gap: 14px; font-size: 20px; letter-spacing: 2.6px; height: 31px; color: #2a2a2a; }
  .contact-list svg { width: 22px; height: 22px; flex: none; }

  .back-band { position: absolute; left: 0; bottom: 0; width: 100%; height: 15px; background: var(--navy-deep); }
</style>
</head>
<body>

<section class="card card-front">
  <div class="front-scene" role="img" aria-label="Darkened photograph of glaciers and mountains in a polar landscape"></div>
  <div class="front-brand">
    <span class="brand-dot"></span>
    <div>
      <div class="brand-name">Frostwyn.co</div>
      <div class="brand-tagline">Polar Expeditions Specialists</div>
    </div>
  </div>
</section>

<section class="card card-back">
  <div class="back-brand">
    <span class="brand-dot"></span>
    <div>
      <div class="brand-name">Frostwyn.co</div>
      <div class="brand-tagline">Polar Expeditions Specialists</div>
    </div>
  </div>

  <div class="divider"></div>

  <div class="contact">
    <div class="contact-name">JONATHAN SMITH</div>
    <div class="contact-role">President/Owner</div>
    <div class="contact-address">123 Anywhere St<br>Any City, ST 12345</div>
    <ul class="contact-list">
      <li>
        <svg viewBox="0 0 24 24" aria-hidden="true"><path d="M6.6 10.8a15 15 0 0 0 6.6 6.6l2.2-2.2c.3-.3.7-.4 1-.2 1.1.4 2.3.6 3.6.6.6 0 1 .4 1 1V20c0 .6-.4 1-1 1A17 17 0 0 1 3 4c0-.6.4-1 1-1h3.5c.6 0 1 .4 1 1 0 1.3.2 2.5.6 3.6.1.3 0 .7-.2 1z" fill="#1c1c1c"/><path d="M14 3a7 7 0 0 1 7 7M14 6.5a3.5 3.5 0 0 1 3.5 3.5" stroke="#1c1c1c" stroke-width="1.8" fill="none" stroke-linecap="round"/></svg>
        413-555-0172
      </li>
      <li>
        <svg viewBox="0 0 24 24" aria-hidden="true"><rect x="2" y="6" width="20" height="13" fill="#1c1c1c"/><path d="M2.5 6.5 12 13.5l9.5-7" stroke="#fff" stroke-width="1.5" fill="none"/></svg>
        youremail@site.com
      </li>
      <li>
        <svg viewBox="0 0 24 24" aria-hidden="true"><circle cx="12" cy="12" r="9.5" fill="none" stroke="#1c1c1c" stroke-width="2"/><ellipse cx="12" cy="12" rx="4" ry="9.5" fill="none" stroke="#1c1c1c" stroke-width="1.6"/><path d="M3 12h18" stroke="#1c1c1c" stroke-width="1.6"/></svg>
        yoursite.com
      </li>
    </ul>
  </div>

  <div class="back-band"></div>
</section>

</body>
</html>
```